Trade Show Display

We need a design for a trade show pop up display. It should incorporate our colors and logo and should complement our other advertising pieces. Our primary brochure is uploaded. Also uploaded is a file with the text to be included and another file with the display dimensions.

```html
<!DOCTYPE html>
<html lang="en">
<head>
<meta charset="utf-8">
<title>Workforce Harbor Partners – Trade Show Display</title>
<link href="https://fonts.googleapis.com/css2?family=Nunito+Sans:wght@400;600&display=swap" rel="stylesheet">
<style>
  :root {
    --navy: #0d3558;
    --green: #86a83a;
    --paper: #ffffff;
    --backdrop: #e6e9ec;
    --photo-a: #c9d6e2;
    --photo-b: #8ea7c0;
  }
  * { margin: 0; padding: 0; box-sizing: border-box; }
  html, body { width: 1200px; height: 844px; overflow: hidden; }
  body {
    background: var(--backdrop);
    font-family: "Nunito Sans", Arial, sans-serif;
    color: var(--navy);
  }
  .display-panel {
    position: absolute;
    left: 120px; top: 18px;
    width: 960px; height: 808px;
    background: var(--paper);
    overflow: hidden;
  }
  .rule { position: absolute; background: var(--green); height: 9px; }
  .rule--top { left: 330px; right: 0; top: 62px; }
  .rule--left { left: 0; width: 160px; top: 150px; }

  .brand { position: absolute; left: 196px; top: 86px; display: flex; align-items: center; gap: 22px; }
  .brand__dot { width: 58px; height: 58px; border-radius: 50%; background: var(--navy); flex: none; }
  .brand__name {
    font-weight: 400; color: var(--navy); white-space: nowrap;
    display: flex; flex-direction: column;
  }
  .brand__line { font-size: 46px; line-height: 50px; letter-spacing: 1px; }
  .brand__line--sub { font-size: 26px; line-height: 32px; letter-spacing: 10px; }

  .tagline {
    position: absolute; left: 0; right: 0; top: 212px;
    text-align: center; font-weight: 600; font-size: 46px; line-height: 56px; color: var(--navy);
  }

  .services { position: absolute; left: 30px; top: 290px; list-style: none; }
  .services__item { display: flex; align-items: center; height: 38px; font-size: 22px; white-space: nowrap; }
  .services__icon {
    width: 30px; height: 30px; border-radius: 50%; background: var(--navy);
    margin-right: 10px; display: flex; align-items: center; justify-content: center; flex: none;
  }
  .services__icon span { width: 14px; height: 14px; border: 2px solid var(--paper); border-radius: 50%; }

  .team-photo { position: absolute; left: 475px; top: 287px; width: 440px; height: 300px; }

  .swoosh { position: absolute; left: 0; top: 540px; width: 960px; height: 130px; }

  .closing {
    position: absolute; left: 0; right: 0; top: 680px;
    text-align: center; color: var(--green); font-size: 36px; line-height: 50px; font-weight: 400;
  }
</style>
</head>
<body>
  <main class="display-panel">
    <div class="rule rule--top"></div>
    <div class="rule rule--left"></div>

    <div class="brand">
      <div class="brand__dot"></div>
      <div class="brand__name">
        <span class="brand__line">WORKFORCE HARBOR</span>
        <span class="brand__line brand__line--sub">PARTNERS</span>
      </div>
    </div>

    <h1 class="tagline">A Trusted Partner for Every Team</h1>

    <ul class="services">
      <li class="services__item"><i class="services__icon"><span></span></i>Talent Acquisition</li>
      <li class="services__item"><i class="services__icon"><span></span></i>Onboarding</li>
      <li class="services__item"><i class="services__icon"><span></span></i>Payroll</li>
      <li class="services__item"><i class="services__icon"><span></span></i>Benefits Management</li>
      <li class="services__item"><i class="services__icon"><span></span></i>Time and Attendance</li>
      <li class="services__item"><i class="services__icon"><span></span></i>Performance Management</li>
      <li class="services__item"><i class="services__icon"><span></span></i>Cafeteria/FSA/HRA Administration</li>
      <li class="services__item"><i class="services__icon"><span></span></i>COBRA Administration</li>
      <li class="services__item"><i class="services__icon"><span></span></i>Human Resource Administration, Compliance Management, and Consulting</li>
    </ul>

    <svg class="team-photo" viewBox="0 0 440 300" role="img" aria-label="Photo of a smiling business team gathered around a laptop in a bright office">
      <defs>
        <linearGradient id="photoTone" x1="0" y1="0" x2="1" y2="1">
          <stop offset="0" stop-color="var(--photo-a)"/>
          <stop offset="1" stop-color="var(--photo-b)"/>
        </linearGradient>
      </defs>
      <path d="M2 2 H438 V205 C420 215 400 240 385 270 C375 292 360 298 340 298 H2 Z" fill="url(#photoTone)" stroke="var(--green)" stroke-width="3"/>
    </svg>

    <svg class="swoosh" viewBox="0 0 960 130" aria-hidden="true">
      <path d="M0 111 H835 C880 111 890 100 905 70 C918 45 935 30 960 28 V42 C940 44 928 56 918 78 C900 116 880 124 835 124 H0 Z" fill="var(--navy)"/>
    </svg>

    <p class="closing">Human Capital Management Solutions<br>for the entire employee Lifecycle</p>
  </main>
</body>
</html>
```